He Lanternway Ridge Podcast is a Top Rated Show dedicated to improving the lives of our brave men and women who serve. Topics about leadership, mental health & resiliency to start living your best life personally and professionally.

Target Market(s)

First Responder Community - Law Enforcement, EMS, Fire Department, Military

Industry/Entity Type

First Responder Community

Requirements
Must have
• I would like my picture and logo to be part of the design. This needs to be formatted for Quillbeam Casts and other platforms
Nice to have
• Some style. Modern Look
Should not have
• N/A

```html
<!DOCTYPE html>
<html lang="en">
<head>
<meta charset="utf-8">
<title>Lanternway Ridge Podcast – Cover Art</title>
<link rel="stylesheet" href="https://fonts.googleapis.com/css2?family=Bebas+Neue&family=Montserrat:wght@400;600;800&family=Mrs+Saint+Delafield&display=swap">
<style>
  :root {
    --page-bg: #e9e9ea;
    --cover-dark: #1c140f;
    --cover-brown: #4a3020;
    --cover-warm: #5e402b;
    --photo-tone-top: #5a3d2a;
    --photo-tone-bottom: #2a1d14;
    --frame: #ffffff;
    --brand-blue: #12a3ea;
    --brand-blue-deep: #0b6fc2;
    --text-white: #ffffff;
    --text-silver: #a9acb2;
  }
  * { margin: 0; padding: 0; box-sizing: border-box; }
  html, body {
    width: 1200px; height: 807px; overflow: hidden;
    background: var(--page-bg);
  }
  .cover {
    position: absolute; left: 220px; top: 23px;
    width: 760px; height: 760px; overflow: hidden;
    background: linear-gradient(120deg, var(--cover-dark) 0%, var(--cover-brown) 55%, var(--cover-warm) 100%);
  }
  .host-photo {
    position: absolute; left: 350px; top: 0; width: 410px; height: 760px;
    background: linear-gradient(180deg, var(--photo-tone-top) 0%, var(--photo-tone-bottom) 100%);
  }
  .frame {
    position: absolute; inset: 24px;
    border: 3px solid var(--frame);
  }
  .brand {
    position: absolute; left: 53px; top: 72px;
  }
  .brand-name {
    display: flex; align-items: center; gap: 10px;
    font-family: "Montserrat", sans-serif; font-weight: 800;
    font-size: 27px; letter-spacing: 1px; color: var(--brand-blue);
  }
  .brand-square {
    width: 16px; height: 16px; background: var(--brand-blue);
  }
  .brand-tagline {
    margin-top: 10px;
    font-family: "Montserrat", sans-serif; font-weight: 600;
    font-size: 10px; letter-spacing: 0.6px; color: var(--text-white);
  }
  .show-title {
    position: absolute; left: 46px; top: 166px;
    font-family: "Bebas Neue", sans-serif; font-weight: 400;
    font-size: 160px; line-height: 118px;
  }
  .show-title span {
    display: block;
    -webkit-background-clip: text; background-clip: text;
    -webkit-text-fill-color: transparent; color: transparent;
  }
  .title-blue {
    background-image: linear-gradient(180deg, var(--brand-blue) 0%, var(--brand-blue) 50%, var(--brand-blue-deep) 68%, var(--brand-blue) 100%);
  }
  .title-white {
    background-image: linear-gradient(180deg, var(--text-white) 0%, var(--text-white) 50%, var(--text-silver) 66%, var(--text-white) 100%);
  }
  .podcast-label {
    position: absolute; left: 48px; top: 542px;
    font-family: "Montserrat", sans-serif; font-weight: 800;
    font-size: 38px; letter-spacing: 39px; color: var(--text-white);
  }
  .host-credit {
    position: absolute; left: 48px; top: 598px;
    display: flex; align-items: baseline; gap: 8px; color: var(--text-white);
  }
  .host-credit .with {
    font-family: "Montserrat", sans-serif; font-weight: 400; font-size: 38px;
  }
  .host-credit .host-name {
    font-family: "Mrs Saint Delafield", cursive; font-size: 92px; line-height: 1;
  }
</style>
</head>
<body>
  <main class="cover">
    <div class="host-photo" role="img" aria-label="Photo of the podcast host in a blue button-up shirt against a warm brown studio backdrop"></div>
    <div class="frame"></div>

    <div class="brand">
      <div class="brand-name"><span class="brand-square"></span>LANTERNWAY RIDGE</div>
      <div class="brand-tagline">LEADERSHIP • COACHING • PERSONAL DEVELOPMENT</div>
    </div>

    <h1 class="show-title">
      <span class="title-blue">LANTERN</span>
      <span class="title-blue">WAY</span>
      <span class="title-white">RIDGE</span>
    </h1>

    <div class="podcast-label">PODCAST</div>

    <div class="host-credit">
      <span class="with">With</span>
      <span class="host-name">Dorian</span>
    </div>
  </main>
</body>
</html>
```